Grand Opening Banner needed for Marvelous Carpets and Home

My website is www.MarvelousCarpetsandHome.com (login with password 'plorka')

A full page banner 1000px X 500px with bright, lively colors and wording that shows an exciting GRAND OPENING celebration throughout the site. Banner needs to convey the following...

Grand Opening Sale
Runs through end of the month
Savings in every department
30 day Returns
Free Rug Pads with every rug
Free shipping.

Banner can be a simple background with graphics and text, or can be a room scene with rugs and furniture, or a grouping of rugs with text.

Some Ideas and Images can be taken from our vendor's websites, such as:

http://tbvendora.com/
http://dosmir.com/dosmir_2015/
http://www.pqmats.com/
http://zaverto.com/
http://shopbelwyn.com/

I also have quite a few room scene images available for use, if you desire.

Target Market(s)

Affluent women who care about stylish decor for their homes

Industry/Entity Type

Home And Garden

Requirements
Must have
• bold, vibrant appearance. Text that can be modified in Photoshop.
Nice to have
• HAND DRAWN, ARTIST STYLE ARTWORK IS GREATLY APPRECIATED.
• flat graphics and text with little to no 3 dimensional (shadow) effect. Font styles should be elegant/luxurious. An organic, scribbled, or painted style is nice in keeping with the handmade products that we sell.
• I am open to changing the color scheme of the website, to match your banner, so don't feel tied down to my existing colors.
Should not have
• nothing too modern or extreme in style.

```html
<!DOCTYPE html>
<html lang="en">
<head>
<meta charset="utf-8">
<title>Grand Opening Sale – Marvelous Carpets and Home</title>
<link href="https://fonts.googleapis.com/css2?family=Bebas+Neue&family=Kaushan+Script&family=Open+Sans:wght@400;600&display=swap" rel="stylesheet">
<style>
  :root {
    --scene-dark: #1b1d20;
    --scene-mid: #3a3d40;
    --scene-rug: #4a4f3c;
    --white: #ffffff;
    --accent-blue: #1f9ee0;
    --sky-blue: #2aa7e8;
    --deep-blue: #1574b0;
  }
  html, body {
    margin: 0;
    padding: 0;
    width: 1200px;
    height: 600px;
    overflow: hidden;
    background: var(--scene-dark);
  }
  .banner {
    position: relative;
    width: 1200px;
    height: 600px;
    overflow: hidden;
    font-family: "Open Sans", Arial, sans-serif;
    color: var(--white);
  }
  .room-photo {
    position: absolute;
    inset: 0;
    background:
      radial-gradient(ellipse at 60% 35%, rgba(120,125,130,0.45) 0%, rgba(0,0,0,0) 55%),
      linear-gradient(180deg, var(--scene-mid) 0%, #2b2e30 45%, var(--scene-rug) 78%, #2a2c22 100%);
  }
  .room-photo::after {
    content: "";
    position: absolute;
    inset: 0;
    background: linear-gradient(90deg, rgba(0,0,0,0.55) 0%, rgba(0,0,0,0.15) 45%, rgba(0,0,0,0.25) 100%);
  }
  .headline {
    position: absolute;
    left: 50px;
    top: 96px;
    margin: 0;
    font-family: "Bebas Neue", Impact, sans-serif;
    font-weight: 400;
    line-height: 0.86;
    font-size: 84px;
    letter-spacing: -2.5px;
  }
  .headline .line { display: block; }
  .headline .line-second { margin-top: 4px; }
  .headline .end-of {
    font-size: 36px;
    letter-spacing: -0.5px;
    color: var(--accent-blue);
    margin-right: 12px;
  }
  .perks {
    position: absolute;
    left: 30px;
    top: 296px;
    width: 370px;
    margin: 0;
    text-align: center;
    font-size: 22px;
    line-height: 30px;
  }
  .offer-shapes {
    position: absolute;
    inset: 0;
  }
  .grand-opening {
    position: absolute;
    left: 910px;
    top: 98px;
    width: 160px;
    text-align: center;
    font-size: 16px;
    line-height: 19px;
    text-transform: uppercase;
  }
  .sale-word {
    position: absolute;
    left: 860px;
    top: 178px;
    width: 220px;
    margin: 0;
    text-align: center;
    font-family: "Kaushan Script", "Brush Script MT", cursive;
    font-weight: 400;
    font-size: 118px;
    line-height: 1.2;
    transform: rotate(-6deg);
  }
  .rug-pad-offer {
    position: absolute;
    left: 876px;
    top: 378px;
    width: 180px;
    text-align: center;
    font-size: 17px;
    line-height: 21px;
  }
  .site-address {
    position: absolute;
    left: 842px;
    top: 558px;
    font-size: 13px;
    font-weight: 600;
    letter-spacing: 0.4px;
    text-transform: uppercase;
  }
</style>
</head>
<body>
  <main class="banner">
    <div class="room-photo" role="img" aria-label="Dim room scene: a woman's legs in black heels seated on a sofa above a patterned rug"></div>

    <h1 class="headline">
      <span class="line">Runs Through</span>
      <span class="line line-second"><span class="end-of">End of</span>The Month</span>
    </h1>

    <p class="perks">Savings in every department<br>30 day Returns</p>

    <svg class="offer-shapes" viewBox="0 0 1200 600" width="1200" height="600" aria-hidden="true">
      <polygon points="990,26 1162,314 802,314" fill="var(--deep-blue)" fill-opacity="0.85"/>
      <polygon points="786,274 1142,274 984,522" fill="var(--sky-blue)"/>
    </svg>

    <div class="grand-opening">Grand<br>Opening</div>
    <p class="sale-word">Sale</p>
    <div class="rug-pad-offer">Free Rug Pads<br>with every rug</div>

    <div class="site-address">www.MarvelousCarpetsandHome.com</div>
  </main>
</body>
</html>
```